MORTENBY ELECTRICAL CONTRACTING - Electrical business

I need a design to go over a new van.
It needs to include;
The logo (All over, you decide)
phone number - 0417356821 (large)
email - bevan@mortenbyelectrical.example (medium)
website - www.mortenbyelectrical.example (small)
EC number - EC58216 (small)
"DOMESTIC & COMMERCIAL" (medium)
The facebook and instagram logos

I have uploaded the new van
my 2 logos
my existing ute as an idea
and a friends ute as another idea (sharp)

```html
<!DOCTYPE html>
<html lang="en">
<head>
<meta charset="utf-8">
<title>Mortenby Electrical Contracting – Van Wrap</title>
<link rel="stylesheet" href="https://fonts.googleapis.com/css2?family=Archivo+Black&family=Montserrat:wght@400;600;700;800&display=swap">
<style>
  :root {
    --stage: #e6e7e8;
    --panel: #ffffff;
    --ink: #111111;
    --ink-soft: #2a2a2a;
    --brand-red: #e31e24;
    --brand-red-dark: #b5151a;
    --white: #ffffff;
  }
  html, body {
    margin: 0;
    padding: 0;
    width: 1200px;
    height: 848px;
    overflow: hidden;
    background: var(--stage);
  }
  .wrap-artwork {
    display: block;
    width: 1200px;
    height: 848px;
  }
  .phone-number {
    font-family: "Archivo Black", "Arial Black", sans-serif;
    font-size: 56px;
    fill: var(--white);
  }
  .service-line {
    font-family: "Montserrat", sans-serif;
    font-weight: 800;
    font-size: 21px;
    letter-spacing: 1px;
    fill: var(--white);
  }
  .email-address {
    font-family: "Montserrat", sans-serif;
    font-weight: 700;
    font-size: 16px;
    fill: var(--white);
  }
  .website-address {
    font-family: "Montserrat", sans-serif;
    font-weight: 700;
    font-size: 22px;
    letter-spacing: 1px;
    fill: var(--white);
  }
  .licence-number {
    font-family: "Montserrat", sans-serif;
    font-weight: 800;
    font-size: 12px;
    fill: var(--white);
  }
  .brand-name {
    font-family: "Montserrat", sans-serif;
    font-weight: 600;
    font-size: 30px;
    letter-spacing: 5px;
    fill: var(--brand-red);
  }
  .brand-descriptor {
    font-family: "Montserrat", sans-serif;
    font-weight: 600;
    font-size: 8.5px;
    letter-spacing: 2.6px;
    fill: var(--white);
  }
  .tagline {
    font-family: "Montserrat", sans-serif;
    font-weight: 400;
    font-size: 18px;
    letter-spacing: 0.5px;
  }
  .tagline-red { fill: var(--brand-red); }
  .tagline-white { fill: var(--white); }
</style>
</head>
<body>
<svg class="wrap-artwork" viewBox="0 0 1200 848" xmlns="http://www.w3.org/2000/svg" role="img" aria-label="Mortenby Electrical Contracting van side wrap artwork">
  <defs>
    <linearGradient id="black-field" x1="0" y1="0" x2="1" y2="1">
      <stop offset="0" stop-color="var(--ink-soft)"/>
      <stop offset="1" stop-color="var(--ink)"/>
    </linearGradient>
    <linearGradient id="red-field" x1="0" y1="1" x2="1" y2="0">
      <stop offset="0" stop-color="var(--brand-red-dark)"/>
      <stop offset="0.5" stop-color="var(--brand-red)"/>
      <stop offset="1" stop-color="var(--brand-red)"/>
    </linearGradient>
    <clipPath id="panel-clip">
      <rect x="40" y="170" width="1120" height="540" rx="24"/>
    </clipPath>
  </defs>

  <rect class="panel-base" x="40" y="170" width="1120" height="540" rx="24" fill="var(--panel)"/>

  <g class="wrap-graphics" clip-path="url(#panel-clip)">
    <!-- red ribbon around the logo panel -->
    <path class="red-ribbon"
          d="M742,505 C752,490 752,460 752,420 L752,380 C752,300 790,262 852,246 L1180,152"
          fill="none" stroke="var(--brand-red)" stroke-width="22"/>

    <!-- main black sweep -->
    <path class="black-sweep"
          d="M20,566 L560,411 C600,400 630,420 650,455 C672,495 695,512 735,508 C770,505 775,470 775,420 L775,380 C775,320 800,290 860,273 L1180,181 L1180,730 L20,730 Z"
          fill="url(#black-field)" stroke="var(--white)" stroke-width="4"/>

    <!-- red phone block -->
    <path class="phone-block"
          d="M60,640 L60,585 L560,441 C595,432 615,450 632,478 C650,510 672,538 720,545 L390,640 Z"
          fill="url(#red-field)"/>
  </g>

  <line class="phone-block-rule" x1="60" y1="650" x2="760" y2="650" stroke="var(--white)" stroke-width="3"/>

  <g class="phone-group" transform="translate(95 632) rotate(-16)">
    <text class="phone-number" x="0" y="0">0417356821</text>
    <line class="phone-underline" x1="150" y1="12" x2="390" y2="12" stroke="var(--white)" stroke-width="4"/>
  </g>

  <text class="licence-number" transform="translate(890 240) rotate(-16)">EC58216</text>

  <g class="brand-block" transform="translate(800 470) rotate(-16)">
    <text class="brand-name" x="0" y="0">MORTENBY</text>
    <text class="brand-descriptor" x="2" y="17">ELECTRICAL CONTRACTING</text>
    <line class="tagline-divider" x1="236" y1="-92" x2="236" y2="-12" stroke="var(--white)" stroke-width="3"/>
    <g class="tagline">
      <text class="tagline-red" x="250" y="-70">AFFORDABLE</text>
      <text class="tagline-white" x="254" y="-46">RELIABLE &amp;</text>
      <text class="tagline-red" x="258" y="-22">FRIENDLY</text>
    </g>
  </g>

  <line class="service-rule" x1="780" y1="515" x2="1160" y2="406" stroke="var(--white)" stroke-width="3"/>
  <line class="service-rule" x1="740" y1="564" x2="1160" y2="444" stroke="var(--white)" stroke-width="3"/>
  <text class="service-line" transform="translate(790 543) rotate(-16)">DOMESTIC &amp; COMMERCIAL</text>

  <text class="email-address" transform="translate(835 625) rotate(-16)">bevan@mortenbyelectrical.example</text>

  <text class="website-address" x="110" y="688">www.mortenbyelectrical.example</text>
  <circle class="social-marker" cx="738" cy="680" r="17" fill="var(--white)"/>
  <circle class="social-marker" cx="784" cy="680" r="17" fill="var(--brand-red)"/>
</svg>
</body>
</html>
```